Digital Transformation Company Trade Show Banners

I am looking for help designing banners for an upcoming trade show. One would be for our company and one would be for our product. I am planning on purchasing retractable banners with a size of 33" x 81". Details are attached.

```html
<!DOCTYPE html>
<html lang="en">
<head>
<meta charset="UTF-8">
<title>Veltrix Technology – Trade Show Banner</title>
<link rel="stylesheet" href="https://fonts.googleapis.com/css2?family=Montserrat:wght@500;600;700;800&display=swap">
<style>
  :root {
    --white: #ffffff;
    --navy-deep: #12151f;
    --navy: #1a2436;
    --steel-blue: #2e5f93;
    --orange: #ee7d2d;
    --sky: #2f97e0;
    --ink: #2b2b2b;
  }
  * { margin: 0; padding: 0; box-sizing: border-box; }
  html, body { width: 1200px; height: 2873px; overflow: hidden; background: var(--white); }
  body { font-family: 'Montserrat', sans-serif; color: var(--white); }

  .banner { position: relative; width: 1200px; height: 2873px; overflow: hidden; }

  .brand-bar {
    position: absolute; top: 0; left: 0; width: 100%; height: 269px;
    background: var(--white);
    display: flex; align-items: center; justify-content: center;
  }
  .brand-name {
    font-weight: 700; font-size: 84px; letter-spacing: 6px;
    color: var(--ink); text-transform: uppercase;
  }

  .main-panel {
    position: absolute; top: 269px; left: 0; width: 100%; height: 2368px;
    background: linear-gradient(180deg, var(--steel-blue) 0%, var(--navy) 30%, var(--navy-deep) 60%, var(--navy-deep) 100%);
  }
  .hero-photo {
    position: absolute; top: 0; left: 0; width: 100%; height: 900px;
    background: radial-gradient(ellipse at 50% 30%, rgba(70,130,190,0.55) 0%, rgba(30,60,100,0.25) 45%, rgba(18,21,31,0) 80%);
  }

  .headline {
    position: absolute; left: 78px; top: 550px;
    font-weight: 700; line-height: 1; text-transform: uppercase;
  }
  .headline .line { display: block; font-size: 142px; margin-bottom: 34px; white-space: nowrap; }
  .headline .accent { color: var(--orange); font-weight: 800; }
  .headline .small { font-size: 104px; }
  .headline-rule {
    position: absolute; left: 100px; top: 1088px; width: 320px; height: 9px; background: var(--orange);
  }

  .offer-intro { position: absolute; left: 74px; top: 1360px; text-transform: uppercase; font-weight: 700; }
  .offer-intro .lead { font-size: 80px; letter-spacing: 2px; }
  .offer-intro .sub { font-size: 46px; margin-left: 24px; }
  .offer-intro .services-title { display: block; color: var(--sky); font-size: 80px; font-weight: 600; margin-top: 4px; }

  .service-list { position: absolute; left: 72px; top: 1590px; list-style: none; }
  .service-item { display: flex; align-items: center; height: 150px; margin-bottom: 44px; }
  .service-icon { width: 140px; height: 140px; flex: none; }
  .service-label {
    margin-left: 94px; font-weight: 600; font-size: 52px; line-height: 1.12; text-transform: uppercase;
  }

  .contact-bar {
    position: absolute; left: 0; bottom: 0; width: 100%; height: 236px;
    background: var(--orange); display: flex; align-items: center;
  }
  .contact-question {
    margin-left: 72px; font-weight: 700; font-size: 54px; line-height: 1.15; text-transform: uppercase;
  }
  .contact-arrow { position: absolute; left: 300px; top: 20px; }
  .contact-details { margin-left: 56px; }
  .contact-row { display: flex; align-items: center; }
  .contact-phone { font-weight: 700; font-size: 74px; }
  .contact-web { font-weight: 500; font-size: 50px; }
  .contact-row svg { margin-right: 26px; flex: none; }
</style>
</head>
<body>
<div class="banner">
  <header class="brand-bar">
    <span class="brand-name">Veltrix Technology</span>
  </header>

  <section class="main-panel">
    <div class="hero-photo" role="img" aria-label="Blue-toned photo of a person in a suit touching a glowing digital interface"></div>

    <h1 class="headline">
      <span class="line">Looking to</span>
      <span class="line"><span class="accent">Thrive</span> <span class="small">in the</span></span>
      <span class="line">Digital Age?</span>
    </h1>
    <div class="headline-rule"></div>

    <p class="offer-intro">
      <span class="lead">We Offer</span><span class="sub">A wide variety of</span>
      <span class="services-title">Digital Services</span>
    </p>

    <ul class="service-list">
      <li class="service-item">
        <svg class="service-icon" viewBox="0 0 140 140" fill="none" stroke="#ee7d2d" stroke-width="5" stroke-linecap="round">
          <circle cx="62" cy="66" r="18"/><circle cx="62" cy="66" r="7"/>
          <path d="M30 60a34 34 0 0 1 52-28M94 72a34 34 0 0 1-52 28"/>
          <path d="M82 32l-2 12M42 100l2-12"/>
          <rect x="92" y="10" width="32" height="40" rx="3"/><path d="M99 22h18M99 31h18M99 40h12"/>
          <rect x="10" y="104" width="34" height="26" rx="3"/><path d="M18 112h18M18 121h18"/>
        </svg>
        <span class="service-label">Digital<br>Transformation</span>
      </li>
      <li class="service-item">
        <svg class="service-icon" viewBox="0 0 140 140" fill="none" stroke="#ee7d2d" stroke-width="5" stroke-linecap="round">
          <circle cx="70" cy="70" r="36"/>
          <rect x="56" y="68" width="28" height="22" rx="3"/><path d="M61 68v-7a9 9 0 0 1 18 0v7"/>
          <path d="M70 34V12M70 106v22M34 70H12M106 70h22M45 45L28 28M95 45l17-17M45 95l-17 17M95 95l17 17"/>
          <circle cx="70" cy="10" r="4"/><circle cx="10" cy="70" r="4"/><circle cx="130" cy="70" r="4"/><circle cx="70" cy="130" r="4"/>
        </svg>
        <span class="service-label">Cybersecurity</span>
      </li>
      <li class="service-item">
        <svg class="service-icon" viewBox="0 0 140 140" fill="none" stroke="#ee7d2d" stroke-width="5" stroke-linecap="round">
          <rect x="12" y="22" width="116" height="80" rx="4"/><path d="M12 88h116M54 102l-6 20M86 102l6 20M40 124h60"/>
          <circle cx="70" cy="58" r="12"/><circle cx="70" cy="58" r="4"/>
          <path d="M30 40h16v10M110 40H94v10M30 76h14M110 76H96"/>
        </svg>
        <span class="service-label">Software<br>Development</span>
      </li>
      <li class="service-item">
        <svg class="service-icon" viewBox="0 0 140 140" fill="none" stroke="#ee7d2d" stroke-width="5" stroke-linecap="round">
          <circle cx="70" cy="72" r="40"/>
          <path d="M70 46a18 18 0 0 0-10 33v9h20v-9a18 18 0 0 0-10-33zM62 96h16"/>
          <path d="M70 32V14M70 112v14M30 72H12M110 72h18M42 44L30 32M98 44l12-12M42 100l-12 12M98 100l12 12"/>
        </svg>
        <span class="service-label">Technology<br>&nbsp;Solution</span>
      </li>
      <li class="service-item">
        <svg class="service-icon" viewBox="0 0 140 140" fill="none" stroke="#ee7d2d" stroke-width="5" stroke-linecap="round">
          <rect x="10" y="10" width="90" height="58" rx="3"/><path d="M22 52l18-18 14 12 22-22 14 10"/>
          <circle cx="114" cy="40" r="10"/><path d="M100 80a14 14 0 0 1 28 0v12"/>
          <circle cx="30" cy="92" r="9"/><circle cx="70" cy="92" r="9"/>
          <path d="M14 130v-14a16 16 0 0 1 32 0v14M54 130v-14a16 16 0 0 1 32 0v14M100 130v-30"/>
        </svg>
        <span class="service-label">Training &amp; Workshops</span>
      </li>
    </ul>
  </section>

  <footer class="contact-bar">
    <svg class="contact-arrow" width="180" height="40" viewBox="0 0 180 40" fill="none" stroke="#ffffff" stroke-width="3" stroke-linecap="round">
      <path d="M10 34Q90 -6 168 26M156 26l12 0-4-12"/>
    </svg>
    <p class="contact-question">Have any<br>questions?</p>
    <div class="contact-details">
      <div class="contact-row">
        <svg width="48" height="48" viewBox="0 0 24 24" fill="none" stroke="#ffffff" stroke-width="1.6" stroke-linejoin="round">
          <path d="M5 3h4l2 5-2.5 1.5a11 11 0 0 0 6 6L16 13l5 2v4a2 2 0 0 1-2 2A16 16 0 0 1 3 5a2 2 0 0 1 2-2z"/>
        </svg>
        <span class="contact-phone">(555) 014-2736</span>
      </div>
      <div class="contact-row">
        <svg width="44" height="44" viewBox="0 0 24 24" fill="none" stroke="#ffffff" stroke-width="1.6">
          <circle cx="12" cy="12" r="10"/><path d="M2 12h20M12 2c3 3 3 17 0 20M12 2c-3 3-3 17 0 20"/>
        </svg>
        <span class="contact-web">www.veltrix.io</span>
      </div>
    </div>
  </footer>
</div>
</body>
</html>
```